Alternative Health Practice - Website redesign

With regard to the welcome image, stock photos can't show the faces of other people. And please don't submit a design for a one-page website.
Hello, I am redesigning a website and need some help from a professional.
The old website is here: peter-lindqvist.net (pls note I don't want to reuse the welcome photo from the old site). Much of the written content will remain the same, so note that I also need a page layout/text colour etc that works for text heavy pages: ie www.peter-lindqvist.net/somatic-articles and www.peter-lindqvist.net/client-reviews
My effort at redesigning is underway here: https://pjlindqvist.sitebuildr.net/my-site-7
The original sitebuildr template is this one: https://www.sitebuildr.net/website-template/view/html/2868?originUrl=https%3A%2F%2Fwww.sitebuildr.net%2Fwebsite%2Ftemplates%2Fhtml%2Fhealth-wellness&tpClick=view_button&esi=6305f015-f1b5-4bdd-8dfa-47b7d756bb68
I'm pretty happy with the colour palette. My name Peter Johan Lindqvist is now the "brand" without Rooted Stillness subtitle. Regarding the Welcome section, if you are going to use my photos, it probably needs to be those two that are already there. If you want to put a stock photo there instead, that's fine.
If you want to propose something quite different to my design, I'm happy to receive design files in Photoshop or whatever and then subsequently replicate on Sitebuildr. Up to you.
Target Market(s)
Mostly women, some men ages 28-60.
Coding
Coded - Design and coding required
Number of Pages Required
5+ page
Look and feel
Each slider illustrates characteristics of the customer's brand and the style your logo design should communicate.

```html
<!DOCTYPE html>
<html lang="en">
<head>
<meta charset="utf-8">
<title>Peter Johan Lindqvist – Somatic Energy Healing</title>
<link href="https://fonts.googleapis.com/css2?family=Inter:wght@400;500&family=Playfair+Display:wght@700&family=Montserrat:wght@500&display=swap" rel="stylesheet">
<style>
  :root{
    --forest:#353a2f;
    --card:#f9f9f8;
    --ink:#151712;
    --gold:#c4962f;
    --leaf:#5f9a3a;
    --white:#ffffff;
    --band:#353a2f;
    --photo-green:#5b6b48;
    --photo-grey:#8a8a88;
  }
  *{box-sizing:border-box;margin:0;padding:0}
  html,body{width:1200px;height:853px;overflow:hidden}
  body{background:var(--forest);font-family:"Inter",sans-serif;color:var(--ink);position:relative}

  .site-header{position:absolute;left:0;top:0;width:1200px;height:77px}
  .brand{position:absolute;left:48px;top:24px;display:flex;align-items:center;gap:14px}
  .brand-dot{width:32px;height:32px;border-radius:50%;background:var(--gold)}
  .brand-name{font-family:"Montserrat",sans-serif;font-weight:500;font-size:15px;letter-spacing:2px;color:var(--gold)}
  .main-nav{position:absolute;left:422px;top:32px;display:flex;gap:21px}
  .main-nav a{color:var(--white);text-decoration:none;font-size:14px;font-weight:500}
  .book-btn{position:absolute;left:1031px;top:23px;width:122px;height:35px;border-radius:18px;background:var(--white);display:flex;align-items:center;gap:7px;padding-left:7px;font-size:13px;color:var(--ink)}
  .arrow-dot{border-radius:50%;background:var(--forest);display:flex;align-items:center;justify-content:center;flex-shrink:0}
  .book-btn .arrow-dot{width:18px;height:18px}

  .hero{position:absolute;left:48px;top:77px;width:1105px;height:720px;background:var(--card);border-radius:33px;overflow:hidden}
  .tag{position:absolute;left:70px;top:185px;height:31px;padding:0 7px 0 6px;border:1px solid var(--ink);border-radius:16px;display:flex;align-items:center;gap:10px;font-size:13px;background:var(--white)}
  .tag-icon{width:19px;height:19px;border-radius:50%;background:#eef3e8;display:flex;align-items:center;justify-content:center}
  .tag-icon span{width:7px;height:7px;border-radius:50%;background:var(--leaf)}
  .hero-title{position:absolute;left:75px;top:218px;font-family:"Playfair Display",serif;font-weight:700;font-size:43px;line-height:44px;color:var(--ink)}
  .hero-text{position:absolute;left:75px;top:330px;width:400px;font-size:20px;line-height:22px;letter-spacing:-0.3px}
  .inline-mark{display:inline-block;width:24px;height:24px;border-radius:50%;background:var(--gold);border:2px solid #f0e2bd;vertical-align:-3px;margin:0 3px}
  .cta{position:absolute;left:75px;top:420px;height:45px;padding:0 8px 0 6px;border-radius:23px;background:var(--white);box-shadow:0 2px 8px rgba(0,0,0,.06);display:flex;align-items:center;gap:7px;font-size:20px;letter-spacing:-0.3px}
  .cta .arrow-dot{width:32px;height:32px}

  .photo{position:absolute;border-radius:12px;box-shadow:0 6px 16px rgba(0,0,0,.15)}
  .photo-back{left:801px;top:238px;width:232px;height:347px;background:linear-gradient(160deg,#b8b8b6,var(--photo-grey) 55%,#3d3d3c)}
  .photo-front{left:722px;top:102px;width:244px;height:348px;background:linear-gradient(150deg,#a9b28a,var(--photo-green) 50%,#3e4a30)}

  .marquee{position:absolute;left:-20px;top:630px;width:1160px;height:40px;background:var(--band);transform:rotate(-1.9deg);display:flex;align-items:center;gap:30px;white-space:nowrap;color:var(--white);font-size:22px;box-shadow:0 14px 14px rgba(0,0,0,.12);
    -webkit-mask-image:linear-gradient(90deg,#000 0,#000 78%,transparent 100%);mask-image:linear-gradient(90deg,#000 0,#000 78%,transparent 100%)}
  .marquee .sep{font-size:20px}
  .marquee .first{margin-left:-17px}
</style>
</head>
<body>
<header class="site-header">
  <div class="brand"><span class="brand-dot"></span><span class="brand-name">PETER LINDQVIST</span></div>
  <nav class="main-nav">
    <a href="#">Home</a><a href="#">The Practice</a><a href="#">About Me</a><a href="#">Approach</a><a href="#">Feedback</a><a href="#">Contact</a>
  </nav>
  <div class="book-btn"><span class="arrow-dot"><svg width="10" height="10" viewBox="0 0 10 10"><path d="M1 5h8M6 2l3 3-3 3" stroke="#fff" stroke-width="1.3" fill="none"/></svg></span>Book a Session</div>
</header>

<main class="hero">
  <div class="tag"><span class="tag-icon"><span></span></span>Somatic Energy Healing</div>
  <h1 class="hero-title">Find Your Inner Balance with<br>Peter Johan Lindqvist</h1>
  <p class="hero-text">Experience Somatic Energy Healing <span class="inline-mark"></span> that aligns your body, mind, and spirit — unlocking clarity, harmony, and lasting well-being.</p>
  <div class="cta"><span class="arrow-dot"><svg width="16" height="16" viewBox="0 0 16 16"><path d="M2 8h12M9 3l5 5-5 5" stroke="#fff" stroke-width="1.8" fill="none"/></svg></span>Begin Your Healing Journey</div>

  <div class="photo photo-back" role="img" aria-label="Black and white photo of a seated person in patterned trousers"></div>
  <div class="photo photo-front" role="img" aria-label="Portrait photo of the practitioner smiling outdoors among green plants"></div>

  <div class="marquee">
    <span class="first">Presence</span><span class="sep">|</span><span>Discovery</span><span class="sep">|</span><span>Creativity</span><span class="sep">|</span><span>Success</span><span class="sep">|</span><span>Ease</span><span class="sep">|</span><span>Harmony</span><span class="sep">|</span><span>Joy</span><span class="sep">|</span><span>Balance</span><span class="sep">|</span><span>Purpose</span>
  </div>
</main>
</body>
</html>
```